" Nome da empresa: Recanto Vivale CLINICA DE NUTRIÇAO SOMOS NUTRICIONISTAS E DESEJAMOS PROPORCIONAR AOS NOSSOS PACIENTES UM TRATAMENTO INDIVIDUALIZADO. FAREMOS ATENDIMENTOS NUTRICIONAIS A FIM DE LEVAR QUALIDADE DE VIDA E PREVENÇAO de doenças, focando na educaçao nutricional "

```html
<!DOCTYPE html>
<html lang="pt-BR">
<head>
<meta charset="UTF-8">
<title>Recanto Vivale – Cartão de visita</title>
<link rel="stylesheet" href="https://fonts.googleapis.com/css2?family=Comfortaa:wght@700&family=Open+Sans:ital,wght@0,400;1,400&display=swap">
<style>
  :root {
    --canvas-bg: #ecebe8;
    --card-white: #ffffff;
    --brand-green: #1f5a4e;
    --brand-gold: #d9a23a;
    --accent-orange: #e8862a;
    --text-light: #ffffff;
  }
  * { margin: 0; padding: 0; box-sizing: border-box; }
  html, body { width: 1200px; height: 1200px; overflow: hidden; }
  body {
    background: var(--canvas-bg);
    position: relative;
    font-family: "Open Sans", Arial, sans-serif;
  }
  .card {
    position: absolute;
    left: 276px;
    width: 648px;
    height: 396px;
    border-radius: 22px;
    box-shadow: 0 6px 18px rgba(0,0,0,0.18);
    overflow: hidden;
  }
  /* Front */
  .card-front { top: 150px; background: var(--card-white); }
  .front-mark {
    position: absolute;
    left: 274px; top: 80px;
    width: 100px; height: 100px;
    border: 3px solid var(--brand-gold);
    border-radius: 50%;
  }
  .front-name {
    position: absolute;
    left: 0; right: 0; top: 200px;
    text-align: center;
    font-family: "Comfortaa", sans-serif;
    font-weight: 700;
    font-size: 50px;
    color: var(--brand-green);
    letter-spacing: 0.5px;
  }
  .front-tagline {
    position: absolute;
    left: 0; right: 0; top: 268px;
    text-align: center;
    font-size: 13px;
    color: var(--brand-green);
  }
  /* Back */
  .card-back { top: 630px; background: var(--brand-green); color: var(--text-light); }
  .back-mark {
    position: absolute;
    left: 40px; top: 83px;
    width: 230px; height: 230px;
    border: 4px solid var(--brand-gold);
    border-radius: 50%;
    display: flex;
    align-items: center;
    justify-content: center;
    text-align: center;
    font-family: "Comfortaa", sans-serif;
    font-weight: 700;
    font-size: 28px;
    line-height: 1.3;
    color: var(--brand-gold);
  }
  .accent-bar {
    position: absolute;
    left: 626px; top: 82px;
    width: 10px; height: 240px;
    background: var(--accent-orange);
  }
  .person-name {
    position: absolute;
    left: 330px; top: 92px;
    font-size: 30px;
  }
  .person-role {
    position: absolute;
    left: 380px; top: 134px;
    font-size: 19px;
    font-style: italic;
  }
  .contact-list {
    position: absolute;
    left: 365px; top: 190px;
    width: 250px;
    list-style: none;
    font-size: 14px;
    line-height: 1.25;
  }
  .contact-list li { margin-bottom: 12px; }
</style>
</head>
<body>
  <section class="card card-front" aria-label="Frente do cartão">
    <div class="front-mark"></div>
    <h1 class="front-name">Recanto Vivale</h1>
    <p class="front-tagline">Saúde-Ciência-Educação Nutricional</p>
  </section>

  <section class="card card-back" aria-label="Verso do cartão">
    <div class="back-mark">Recanto<br>Vivale</div>
    <div class="accent-bar"></div>
    <h2 class="person-name">Nome Sobrenome</h2>
    <p class="person-role">Função</p>
    <ul class="contact-list">
      <li>Tel:0000-0000</li>
      <li>Cel:0000-0000</li>
      <li>Email:ola@recantovivale.com.br</li>
      <li>Endereço:Rua dos Ipês,00 Bairro Pomar, Cidade Serena</li>
    </ul>
  </section>
</body>
</html>
```